Brochure for business coaching company
Velmora Tidewell
Maybe tri-fold or other. We would like a modern uplifting design.
Consulting
Busy professionals, entrepreneurs, corporate executives, leaders wishing to enhance their leadership skills, communication skills, influence skills, marketing skills. Individuals wanting to uncover their life's potential as well as creating more balance and fulfillment in their life.
Brochure will explain what we do. It should also create the desire to use our services because working with us is a smart move.
It will help your career, your life, and your business. It will give you the edge to raise above the competition and take your business or career to the next level. We teach the entrepreneurial and leadership skills and techniques you need to run a remarkable business using our unique three phase "w$ndle" program. Our expertise has its foundation in leading edge scientific research in human potential. This approach will help program your mind for success in everything you do. We designed the system to give you all the skills, tools, and techniques you need to run a prosperous enterprise. We then provide the structure to give you a powerful success network to support and guide you. You will be inspired, energized and championed every step of the way.

```html
<!DOCTYPE html>
<html lang="en">
<head>
<meta charset="utf-8">
<title>Velmora Tidewell – Business Coaching Brochure</title>
<link rel="stylesheet" href="https://fonts.googleapis.com/css2?family=Open+Sans:wght@400;600;700;800&display=swap">
<style>
  :root {
    --brand-blue: #2b6fb6;
    --brand-blue-deep: #1f5a9a;
    --white: #ffffff;
    --ink: #1c2430;
    --canvas: #eef0f3;
    --sky-top: #8fb6dc;
    --sky-low: #d9e6f2;
    --rock: #9a948c;
    --meeting-dark: #3a3f47;
    --meeting-light: #c9c6c1;
  }
  * { box-sizing: border-box; margin: 0; padding: 0; }
  html, body {
    width: 1200px; height: 1055px; overflow: hidden;
    background: var(--canvas);
    font-family: "Open Sans", Arial, sans-serif;
  }
  .spread {
    position: absolute; left: 50px; width: 1100px; height: 480px;
    display: flex; box-shadow: 0 4px 14px rgba(0,0,0,.18);
  }
  .spread--outside { top: 30px; }
  .spread--inside { top: 545px; }
  .panel { position: relative; width: 550px; height: 100%; overflow: hidden; }
  .panel--blue { background: var(--brand-blue); color: var(--white); }

  .body-copy { font-size: 12px; line-height: 1.6; }
  .photo { position: absolute; }

  /* Outside spread – back panel */
  .back .body-copy { position: absolute; left: 40px; top: 36px; width: 470px; }
  .back .photo { left: 40px; top: 150px; width: 300px; height: 150px;
    background: linear-gradient(135deg, #d7d3cc, #8d8a86 60%, #3d434c); }
  .back .brand-title { position: absolute; left: 40px; top: 338px;
    font-size: 34px; font-weight: 800; }
  .back .contact-line { position: absolute; left: 40px; top: 392px; font-size: 13px; font-weight: 600; }

  /* Outside spread – cover panel */
  .cover .photo { inset: 0;
    background: linear-gradient(100deg, var(--sky-top) 0%, var(--sky-low) 45%, var(--rock) 70%, #6f6a63 100%); }
  .cover .cover-heading { position: absolute; left: 60px; top: 62px; color: var(--white); }
  .cover .cover-heading strong { display: block; font-size: 46px; font-weight: 800; letter-spacing: 1px; }
  .cover .cover-heading span { display: block; font-size: 15px; margin-top: 4px; }
  .cover .brand-lockup { position: absolute; left: 60px; top: 200px; display: flex; align-items: center; gap: 10px;
    color: var(--brand-blue-deep); font-size: 24px; font-weight: 700; }
  .brand-mark { width: 22px; height: 22px; background: var(--brand-blue-deep); }
  .cover .contact-line { position: absolute; left: 60px; bottom: 26px; font-size: 12px; font-weight: 600; color: var(--ink); }

  /* Inside spread – left panel */
  .intro .brand-title { position: absolute; left: 40px; top: 34px; font-size: 30px; font-weight: 800; }
  .intro .body-copy--top { position: absolute; left: 40px; top: 90px; width: 470px; }
  .intro .photo-pair { position: absolute; left: 40px; top: 190px; display: flex; gap: 14px; }
  .intro .photo-pair .photo { position: static; width: 228px; height: 140px;
    background: linear-gradient(135deg, #dcd8d1, #8e8b87 60%, #3b414a); }
  .intro .body-copy--bottom { position: absolute; left: 40px; top: 356px; width: 470px; }

  /* Inside spread – right panel */
  .feature .photo { inset: 0;
    background: linear-gradient(160deg, var(--meeting-light) 0%, #8a8a8c 40%, var(--meeting-dark) 100%); }
  .feature .feature-band { position: absolute; left: 0; right: 0; top: 280px; padding: 12px 40px;
    background: rgba(20,24,32,.72); color: var(--white); }
  .feature .feature-band h2 { font-size: 20px; font-weight: 700; letter-spacing: .5px; margin-bottom: 8px; }
  .feature .feature-band p { font-size: 12px; line-height: 1.6; }
</style>
</head>
<body>

<section class="spread spread--outside">
  <div class="panel panel--blue back">
    <p class="body-copy">We help busy professionals, entrepreneurs and executives grow the leadership, communication and influence skills they need. Our coaching is built on research in human potential and gives you the tools, structure and support to move your career and business to the next level with clarity and balance.</p>
    <div class="photo" role="img" aria-label="Photo of a business team meeting around a table"></div>
    <h2 class="brand-title">Velmora Tidewell</h2>
    <p class="contact-line">Mobile: 1234567890 email: hello@velmoratidewell.com</p>
  </div>
  <div class="panel cover">
    <div class="photo" role="img" aria-label="Photo of a businessman climbing a rock face against a blue sky"></div>
    <div class="cover-heading">
      <strong>BUSINESS</strong>
      <span>Coaching Company</span>
    </div>
    <div class="brand-lockup"><span class="brand-mark"></span>Velmora Tidewell</div>
    <p class="contact-line">Mobile: 1234567890 email: hello@velmoratidewell.com</p>
  </div>
</section>

<section class="spread spread--inside">
  <div class="panel panel--blue intro">
    <h2 class="brand-title">Velmora Tidewell</h2>
    <p class="body-copy body-copy--top">Working with us is a smart move. Our three phase w$ndle program teaches the entrepreneurial and leadership techniques you need to run a remarkable business and program your mind for success.</p>
    <div class="photo-pair">
      <div class="photo" role="img" aria-label="Photo of a business meeting at a conference table"></div>
      <div class="photo" role="img" aria-label="Photo of colleagues discussing plans in an office"></div>
    </div>
    <p class="body-copy body-copy--bottom">We then give you a powerful success network to support and guide you. You will be inspired, energized and championed every step of the way.</p>
  </div>
  <div class="panel feature">
    <div class="photo" role="img" aria-label="Overhead photo of executives working together with laptops and documents"></div>
    <div class="feature-band">
      <h2>BUSINESS COACHING COMPANY</h2>
      <p>It will help your career, your life and your business. Gain the edge to rise above the competition and take your work to the next level.</p>
    </div>
  </div>
</section>

</body>
</html>
```